Flyer-Design für Großhandel für techn. Gase
Zielgruppe
Wir sind ein Großhandel für techn. Gase. Ebenso haben wir einen Ballonshop, den wir gerne per Flyer bewerben würden. Zielgruppe sind in erster Linie Familien. Der Flyer wird aber an alles Haushalte verschickt und soll grundsätzlich alle Zielgruppen ansprechen, da jeder zu unterschiedlichen Events Ballons verschenkt.
Aufgabenstellung
Format DIN 5, beidseitig bedruckt ( vorne+hinten), Man soll dem Flyer auf der ersten Blick entnehmen können, dass es sich um einen Ballonshop handelt. Ebenso soll daraus hervorgehen, dass man den Shop besuchen kann und nicht nur online Bestellungen möglich sind. Diverese Ballon-Abbildungen sind sicherlich hilfreich. Ebenso würde ich auch ein paar fliegende GUmmiballons mit einbringen. Im Anhang erhalten Sie einen Flyer, den wir mal entworfen hatten und den wir so intern verwendet haben. Leider ist dieser nicht wirklich professionell :-) Des weiteren erhalten Sie auch noch ein Bild von unserem Shop. Der Flyer sollte auch ersichtlich machen, dass man auch das Helium/Ballongas an sich bei uns beziehen kann. Fly

```html
<!DOCTYPE html>
<html lang="de">
<head>
<meta charset="utf-8">
<title>Ballonshop Flyer – Vorder- und Rückseite</title>
<link href="https://fonts.googleapis.com/css2?family=Bangers&family=Hind:wght@500;600;700&display=swap" rel="stylesheet">
<style>
  :root {
    --stage: #5c6558;
    --navy: #26446e;
    --navy-deep: #1f3a64;
    --cream: #e7e3d2;
    --cream-light: #f3f1e7;
    --silver: #ece7cf;
    --white: #ffffff;
    --magenta: #b0268f;
    --yellow: #f2b417;
    --red: #d9262f;
    --sky: #3aa8e0;
    --pink: #e58fb4;
    --rose: #d81b74;
    --orange: #e8650f;
  }
  * { box-sizing: border-box; margin: 0; padding: 0; }
  html, body { width: 1200px; height: 774px; overflow: hidden; background: var(--stage); }
  .canvas { position: relative; width: 1200px; height: 774px; }

  .flyer {
    position: absolute; top: 104px; width: 426px; height: 602px;
    background: var(--navy); overflow: hidden;
    font-family: "Bangers", "Comic Sans MS", cursive;
  }
  .flyer--front { left: 139px; }
  .flyer--back { left: 639px; }

  .abs { position: absolute; line-height: 1; white-space: nowrap; }
  .art { position: absolute; }

  /* front headline */
  .headline { position: absolute; inset: 0; z-index: 2; pointer-events: none; }
  .balloon-letter {
    position: absolute; line-height: 1; font-size: 84px;
    -webkit-text-stroke: 5px var(--white); paint-order: stroke fill;
  }
  .bl-b  { left: 30px;  top: 40px; color: var(--magenta); transform: rotate(-6deg); }
  .bl-a  { left: 100px; top: 22px; color: var(--yellow);  transform: rotate(-4deg); }
  .bl-l1 { left: 170px; top: 54px; color: var(--red);     transform: rotate(-8deg); }
  .bl-l2 { left: 214px; top: 24px; color: var(--sky);     transform: rotate(-10deg); }
  .bl-o  { left: 260px; top: 10px; color: var(--pink);    transform: rotate(4deg); }
  .bl-n  { left: 326px; top: 44px; color: var(--rose);    transform: rotate(10deg); }
  .shop-word { left: 254px; top: 122px; font-size: 44px; color: var(--white); letter-spacing: 3px; }

  .cluster-art { left: 22px; top: 112px; width: 170px; height: 236px; border-radius: 60px 60px 80px 40px;
    background: radial-gradient(circle at 35% 30%, #3aa8e0, #d9264f 45%, #f08c1e 70%, #9b4fb0 100%); opacity: .85; }

  .bunte { position: absolute; left: 206px; top: 196px; display: flex; align-items: flex-end; font-size: 60px; line-height: 1; z-index: 2; }
  .bunte span { -webkit-text-stroke: 3px var(--white); paint-order: stroke fill; display: inline-block; }
  .bunte .c1 { color: #e0338f; transform: translateY(6px) rotate(-6deg); }
  .bunte .c2 { color: var(--orange); transform: translateY(-4px) rotate(-4deg); }
  .bunte .c3 { color: #1f9fdc; transform: translateY(2px); }
  .bunte .c4 { color: #f3c21b; transform: translateY(-10px) rotate(4deg); }
  .bunte .c5 { color: #e22a2a; transform: translateY(-6px) rotate(2deg); }

  .motiv { right: 24px; top: 256px; font-size: 46px; color: var(--white); transform: rotate(-3deg); letter-spacing: 1px; z-index: 2; }
  .helium { right: 22px; top: 300px; font-size: 40px; color: var(--white); letter-spacing: 1px; z-index: 2; }
  .visit { left: 88px; top: 350px; font-size: 34px; color: var(--white); letter-spacing: 1px; z-index: 2; }
  .visit-shop { left: 208px; top: 384px; font-size: 31px; color: var(--white); letter-spacing: 1px; z-index: 2; }

  .band { position: absolute; left: 0; width: 426px; }
  .front-band { top: 396px; height: 170px; }
  .shop-photo { left: 29px; top: 406px; width: 200px; height: 154px;
    background: linear-gradient(160deg, #6f5a3d, #c79a5c 50%, #e2c9a4); border-radius: 4px; }
  .star-art { left: 122px; top: 388px; width: 68px; height: 68px;
    background: linear-gradient(135deg, #c77ad4, #8a3ea6);
    clip-path: polygon(50% 0, 61% 35%, 98% 35%, 68% 57%, 79% 91%, 50% 70%, 21% 91%, 32% 57%, 2% 35%, 39% 35%); }
  .brand { position: absolute; right: 20px; top: 462px; display: flex; align-items: center; gap: 8px;
    font-family: "Hind", sans-serif; font-weight: 700; font-size: 26px; line-height: 1; color: var(--navy-deep); }
  .brand-mark { width: 16px; height: 16px; background: var(--navy-deep); }
  .address { position: absolute; right: 18px; top: 510px; text-align: right;
    font-family: "Hind", sans-serif; font-weight: 600; font-size: 18px; line-height: 25px; color: var(--navy-deep); }
  .contact { position: absolute; left: 0; right: 0; display: flex; justify-content: center;
    font-family: "Hind", sans-serif; font-weight: 600; color: var(--white); }
  .front-contact { top: 576px; font-size: 14px; gap: 16px; }

  /* back */
  .back-title { left: 36px; top: 26px; font-size: 62px; color: var(--silver); letter-spacing: 2px; transform: rotate(-4deg); transform-origin: left bottom; }
  .back-sub { left: 0; right: 0; text-align: center; font-size: 28px; color: var(--silver); letter-spacing: 1px; }
  .back-sub--1 { top: 92px; }
  .back-sub--2 { top: 120px; }
  .balloons-art { left: 24px; top: 150px; width: 380px; height: 266px; border-radius: 40px;
    background: radial-gradient(circle at 30% 30%, #f2d43a 0, transparent 22%),
                radial-gradient(circle at 50% 55%, #d9a75a 0, transparent 30%),
                radial-gradient(circle at 85% 30%, #e8e8f0 0, transparent 22%),
                linear-gradient(135deg, #c24a4a, #c9974b 50%, #7ea6d8); opacity: .75; }
  .back-band { top: 384px; height: 154px; }
  .navy-text { color: var(--navy-deep); }
  .occasion-head { left: 14px; top: 436px; font-size: 23px; letter-spacing: .5px; }
  .occasions { left: 320px; top: 434px; font-size: 16px; line-height: 16px; text-align: center; }
  .zahlen { left: 14px; top: 470px; font-size: 21px; }
  .zahlen-note { left: 13px; top: 493px; font-family: "Hind", sans-serif; font-weight: 600; font-size: 11px; line-height: 15px; }
  .geschenk { left: 160px; top: 478px; font-size: 21px; transform: rotate(-3deg); }
  .bouquets { left: 190px; top: 512px; font-size: 21px; }
  .helium-note { left: 0; right: 0; top: 547px; text-align: center; font-size: 15px; line-height: 17px; color: var(--cream-light); letter-spacing: .5px; }
  .back-contact { top: 580px; font-size: 11px; gap: 12px; }
</style>
</head>
<body>
<main class="canvas">

  <section class="flyer flyer--front">
    <div class="art cluster-art" role="img" aria-label="Bunte Latex- und Sternballons"></div>
    <h1 class="headline" aria-label="Ballon Shop">
      <span class="balloon-letter bl-b">B</span>
      <span class="balloon-letter bl-a">A</span>
      <span class="balloon-letter bl-l1">L</span>
      <span class="balloon-letter bl-l2">L</span>
      <span class="balloon-letter bl-o">O</span>
      <span class="balloon-letter bl-n">N</span>
      <span class="abs shop-word">SHOP</span>
    </h1>
    <p class="bunte"><span class="c1">B</span><span class="c2">U</span><span class="c3">N</span><span class="c4">T</span><span class="c5">E</span></p>
    <p class="abs motiv">MOTIVBALLONS</p>
    <p class="abs helium">MIT HELIUM</p>
    <p class="abs visit">BESUCHEN SIE UNSEREN</p>
    <p class="abs visit-shop">SHOP!</p>

    <svg class="band front-band" viewBox="0 0 426 170" preserveAspectRatio="none" aria-hidden="true">
      <defs>
        <linearGradient id="creamFront" x1="0" y1="0" x2="1" y2="1">
          <stop offset="0" stop-color="#f3f1e7"/><stop offset=".5" stop-color="#dedac6"/><stop offset="1" stop-color="#ece9dc"/>
        </linearGradient>
      </defs>
      <path d="M0 60 Q0 30 30 30 L300 18 Q390 2 410 2 Q426 4 426 20 L426 150 Q426 164 410 164 L20 164 Q0 164 0 150 Z" fill="url(#creamFront)"/>
    </svg>
    <div class="art shop-photo" role="img" aria-label="Foto des Ballonshops mit Ballons und Grußkarten"></div>
    <div class="art star-art" role="img" aria-label="Lila Sternfolienballon"></div>
    <div class="brand"><span class="brand-mark"></span>BRANDGAS</div>
    <p class="address">Voltastraße 12,<br>64521 Talheim</p>
    <p class="contact front-contact"><span>Tel: 06123/45678-0</span><span>www.brandgas.de</span><span>info@brandgas.de</span></p>
  </section>

  <section class="flyer flyer--back">
    <h2 class="abs back-title">FOLIENBALLONS</h2>
    <p class="abs back-sub back-sub--1">IN VIELEN VERSCHIEDENEN</p>
    <p class="abs back-sub back-sub--2">FARBEN UND FORMEN</p>

    <svg class="band back-band" viewBox="0 0 426 154" preserveAspectRatio="none" aria-hidden="true">
      <defs>
        <linearGradient id="creamBack" x1="0" y1="0" x2="1" y2="1">
          <stop offset="0" stop-color="#f3f1e7"/><stop offset=".5" stop-color="#dedac6"/><stop offset="1" stop-color="#ece9dc"/>
        </linearGradient>
      </defs>
      <path d="M0 40 Q0 28 20 28 L300 18 Q390 2 410 2 Q426 4 426 18 L426 140 Q426 152 410 152 L16 152 Q0 152 0 140 Z" fill="url(#creamBack)"/>
    </svg>
    <div class="art balloons-art" role="img" aria-label="Folienballons: Happy-Birthday-Ballon, Zahlen 30 und 2021, Einhorn, Herz, Sterne, Konfettiballons und Kinderwagen"></div>

    <p class="abs navy-text occasion-head">PASSENDEN BALLONS FÜR JEDE</p>
    <p class="abs navy-text occasions">PARTY<br>GEBURTSTAG<br>JUBILÄUM<br>HOCHZEIT</p>
    <p class="abs navy-text zahlen">ZAHLENBALLONS</p>
    <p class="abs navy-text zahlen-note">in Pink, Blau, Gold,<br>Silber, Rosegold</p>
    <p class="abs navy-text geschenk">GESCHENKBALLONS</p>
    <p class="abs navy-text bouquets">BALLON-BOUQUETS</p>
    <p class="abs helium-note">SIE KÖNNEN AUCH DAS HELIUM/BALLONGAS<br>AN SICH BEI UNS BEZIEHEN.</p>
    <p class="contact back-contact"><span>Tel: 06123/45678-0</span><span>www.brandgas.de</span><span>info@brandgas.de</span></p>
  </section>

</main>
</body>
</html>
```